Pellmark Ridgeway LLC stationery, business card and web page design.

i need a full set of stationery designed using the name "Pellmark Ridgeway LLC" with a tag line "construction consulting services". using the uploaded monkey icon as the logo.

i like the colors orange, green and black in general but im not limited to that. the company offers consulting services to various types of construction businesses.

i travel around the country in a 4x4 camper offering consulting services and technical training short term and long to various types of construction companies.

Construction Company

Peter Lund
p.lund@pellmarkridgeway.example
2748 Fenwick Rd
Maple Glen, NY 10943
555 014 3627

list these services on the card.

Business Consulting
Capital Investments
Marketing Implementations
Technical Training

1 page

Designer to choose colors to be used in the design.

• company info and use of the monkey icon i provided.
• a fun but professional design
• the color red

```html
<!DOCTYPE html>
<html lang="en">
<head>
<meta charset="utf-8">
<title>Pellmark Ridgeway LLC – Business Card</title>
<link href="https://fonts.googleapis.com/css2?family=Cormorant+Garamond:wght@500&family=Open+Sans:wght@400;600&display=swap" rel="stylesheet">
<style>
  :root {
    --page-bg: #4a423e;
    --card-black: #141414;
    --card-edge: #1e1e1e;
    --gloss: #6a6a6a;
    --gloss-dim: #4d4d4d;
    --ink-white: #ffffff;
    --accent-orange: #f26a21;
    --divider: #9a9a9a;
  }
  * { box-sizing: border-box; margin: 0; padding: 0; }
  html, body {
    width: 1200px; height: 864px; overflow: hidden;
    background: var(--page-bg);
  }
  .canvas {
    position: relative; width: 1200px; height: 864px;
    display: flex; align-items: center; justify-content: center; gap: 50px;
  }
  .card {
    position: relative; width: 525px; height: 300px;
    background: var(--card-black);
    border: 1px solid var(--card-edge);
    box-shadow: 0 14px 30px rgba(0,0,0,.45);
    overflow: hidden;
  }

  /* back side */
  .card-back { display: flex; flex-direction: column; align-items: center; }
  .back-mark {
    margin-top: 46px; width: 96px; height: 96px; border-radius: 50%;
    background: radial-gradient(circle at 40% 35%, #5a5a5a, #2a2a2a 70%);
  }
  .back-name {
    margin-top: 16px;
    font-family: "Cormorant Garamond", serif; font-weight: 500;
    font-size: 27px; letter-spacing: 1px; text-transform: uppercase;
    color: var(--gloss);
  }
  .back-tagline {
    margin-top: 2px;
    font-family: "Cormorant Garamond", serif; font-weight: 500;
    font-size: 12px; letter-spacing: 1.5px; text-transform: uppercase;
    color: var(--gloss-dim);
  }
  .back-web {
    margin-top: 24px;
    font-family: "Open Sans", sans-serif; font-size: 15px;
    letter-spacing: 7px; color: var(--gloss);
  }

  /* front side */
  .card-front { display: flex; align-items: center; }
  .brand {
    width: 230px; display: flex; flex-direction: column; align-items: center; gap: 14px;
  }
  .brand-mark { width: 120px; height: 120px; border-radius: 50%; background: var(--ink-white); }
  .brand-name {
    font-family: "Open Sans", sans-serif; font-weight: 600; font-size: 14px;
    color: var(--ink-white); letter-spacing: .5px;
  }
  .divider {
    width: 1px; height: 180px;
    background: linear-gradient(to bottom, transparent, var(--divider) 25%, var(--divider) 75%, transparent);
  }
  .contact {
    padding-left: 22px;
    font-family: "Open Sans", sans-serif; color: var(--ink-white);
    font-size: 14px; line-height: 1.3;
  }
  .contact-name {
    font-weight: 600; font-size: 17px; color: var(--accent-orange); text-transform: uppercase;
  }
  .contact-title { font-size: 15px; margin-bottom: 10px; }
  .contact-address { margin-bottom: 6px; }
  .contact-list { list-style: none; }
  .contact-list li { display: flex; align-items: center; gap: 8px; }
  .contact-list svg { width: 11px; height: 11px; fill: var(--accent-orange); flex: none; }
  .contact-web { padding-left: 19px; }
</style>
</head>
<body>
<main class="canvas">

  <section class="card card-back">
    <div class="back-mark" role="img" aria-label="Embossed company mark"></div>
    <h1 class="back-name">Pellmark Ridgeway LLC</h1>
    <p class="back-tagline">Construction Consulting Services</p>
    <p class="back-web">www.pellmarkridgeway.example</p>
  </section>

  <section class="card card-front">
    <div class="brand">
      <div class="brand-mark" role="img" aria-label="Company mark"></div>
      <span class="brand-name">Pellmark Ridgeway LLC</span>
    </div>
    <div class="divider"></div>
    <div class="contact">
      <p class="contact-name">Peter Lund</p>
      <p class="contact-title">CEO/FOUNDER</p>
      <p class="contact-address">2748 Fenwick Rd<br>Maple Glen, NY 10943</p>
      <ul class="contact-list">
        <li><svg viewBox="0 0 12 12"><path d="M1 3c0-1 1-2 2-2h6c1 0 2 1 2 2v1H8V3H4v1H1z M2 5h8l1 6H1z"/></svg>555 014 3627</li>
        <li><svg viewBox="0 0 12 12"><path d="M3 0h6v12H3z M4 1v8h4V1z"/></svg>555 014 8821</li>
        <li><svg viewBox="0 0 12 12"><path d="M3 0h6v4H3z M0 4h12v8H0z"/></svg>555 014 5096</li>
        <li><svg viewBox="0 0 12 12"><path d="M0 2h12v8H0z M1 3l5 4 5-4z" fill-rule="evenodd"/></svg>p.lund@pellmarkridgeway.example</li>
        <li><svg viewBox="0 0 12 12"><circle cx="6" cy="6" r="6"/></svg>www.pellmarkridgeway.example</li>
      </ul>
    </div>
  </section>

</main>
</body>
</html>
```